3D Printing Business coming soon page

Hi we are looking for a one page "coming soon" website for our business. The business is called "Solevia Labs" and it is a new solution which 3D Prints Orthotics (Insoles).

The design should include our logo, an improved version of our promotional image (attached), a web form for capturing interest from people, a countdown timer and some text.

Follow the colour scheme which is shown in our logo along with our other colours - Orange (RGB#ff8300) and Light Green (RGB#30f20a)
Updates

Industry/Entity Type

Business

Font styles to use
Sans Serif

Requirements
Must have
• Logo (Attached)
Improved version of Promotional Image
Web Form design for capturing Name, EMail Address and Comments along with a Turin test
Countdown Timer
Text - "Solevia Labs will shake up the Orthotics Industry. Foot Orthosis patient-ready in hours for a fraction of the price you are paying today. Welcome to the new world of 3D Printing!"

```html
<!DOCTYPE html>
<html lang="en">
<head>
<meta charset="utf-8">
<title>Solevia Labs — Coming Soon</title>
<link href="https://fonts.googleapis.com/css2?family=Cabin:wght@400;500&family=Open+Sans:wght@600&family=Roboto:wght@400&display=swap" rel="stylesheet">
<style>
:root{
  --navy:#0b3f8a;
  --blue:#1a86c4;
  --blue-dark:#0a5e94;
  --green-bright:#30f20a;
  --green-ball:#8cc83a;
  --green-ball-dark:#5f9a1a;
  --ink:#2f2f2f;
  --sky-top:#ffffff;
  --sky-bottom:#8fc4ea;
  --paper:#ffffff;
  --footer-bg:#f6f6f6;
  --field-line:#d8d8d8;
  --muted:#8a8a8a;
}
*{margin:0;padding:0;box-sizing:border-box}
html,body{width:1200px;height:1008px;overflow:hidden;background:var(--paper)}
body{position:relative;font-family:"Cabin",sans-serif;color:var(--navy)}
.abs{position:absolute}

.top-bar,.bottom-bar{position:absolute;left:0;width:1200px;height:6px;background:var(--green-bright)}
.top-bar{top:0}
.bottom-bar{bottom:0;height:15px}

.hero{position:absolute;left:0;top:6px;width:1200px;height:532px;
  background:linear-gradient(180deg,var(--sky-top) 0%,#e6f1fa 25%,#b6d8f1 60%,var(--sky-bottom) 100%)}

.social{position:absolute;top:33px;left:840px;display:flex;gap:18px}
.social-dot{width:41px;height:41px;border-radius:50%;display:flex;align-items:center;justify-content:center}
.social-dot.one{background:#1e67b3}
.social-dot.two{background:#6cb6df}
.social-dot.three{background:#4aa98c}

.brand{position:absolute;left:170px;top:150px;display:flex;align-items:center;gap:16px}
.brand-dot{width:64px;height:64px;border-radius:50%;background:var(--blue)}
.brand-name{font-family:"Cabin",sans-serif;font-weight:500;font-size:50px;color:var(--blue-dark);line-height:1}

.welcome{position:absolute;left:580px;top:105px;width:430px;text-align:center;font-size:27px;line-height:30px;color:var(--navy)}
.coming-soon{position:absolute;left:570px;top:170px;font-family:"Open Sans",sans-serif;font-weight:600;font-size:78px;color:var(--ink);letter-spacing:-1px;line-height:1}

.countdown{position:absolute;top:266px;left:615px;display:flex;gap:12px}
.tick{width:80px;height:80px;border-radius:50%;display:flex;flex-direction:column;align-items:center;justify-content:center;
  font-family:"Roboto",sans-serif;line-height:1;box-shadow:0 6px 6px -3px rgba(0,0,0,.18)}
.tick .num{font-size:29px}
.tick .unit{font-size:14px;margin-top:1px}
.tick.days{background:radial-gradient(circle at 40% 30%,#3aa6db,var(--blue-dark) 75%);color:#fff;border:2px solid #0a5680}
.tick.lime{background:radial-gradient(circle at 40% 30%,#c6ec5a,var(--green-ball) 70%);color:var(--navy);border:2px solid var(--green-ball-dark)}

.turing-btn{position:absolute;left:686px;top:369px;width:207px;height:46px;background:var(--navy);border-radius:2px;display:flex;align-items:center;gap:10px;padding-left:10px;color:#fff}
.turing-btn .small{font-size:11px;line-height:1;display:block}
.turing-btn .big{font-size:24px;line-height:1;display:block;letter-spacing:-.5px}

.steps{position:absolute;left:0;top:430px;width:1200px}
.step{position:absolute;top:0;width:201px}
.step-photo{width:201px;height:201px;border-radius:50%;border:6px solid #e4e4e4;box-shadow:0 0 0 1px #cfcfcf,0 8px 10px -6px rgba(0,0,0,.25)}
.step-num{position:absolute;left:-24px;top:134px;width:53px;height:53px;border-radius:50%;background:var(--navy);color:#fff;font-size:25px;display:flex;align-items:center;justify-content:center}
.step-label{position:absolute;top:214px;left:-40px;width:281px;text-align:center;font-size:24px;line-height:29px;color:var(--navy)}
.s1{left:165px}.s2{left:392px}.s3{left:623px}.s4{left:852px}
.photo-scan{background:radial-gradient(circle at 50% 45%,#f4f4f4,#c9ccd0 75%)}
.photo-design{background:radial-gradient(circle at 50% 55%,#f0a08a 0%,#f6f6f6 35%,#e6e8ec 80%)}
.photo-print{background:radial-gradient(circle at 50% 45%,#9ad0e8 0%,#d9d9d4 45%,#e9e9e6 80%)}
.photo-fit{background:radial-gradient(circle at 55% 50%,#e3c58f 0%,#7a5a4a 40%,#f2f2f2 70%)}

.notify{position:absolute;left:0;top:716px;width:1200px;height:277px;background:var(--footer-bg)}
.notify-title{position:absolute;left:540px;top:20px;width:393px;text-align:center;font-size:20px;color:var(--navy);letter-spacing:-.3px}
.pitch{position:absolute;left:174px;top:58px;width:300px;font-size:19.5px;line-height:26px;color:var(--blue-dark)}
.copyright{position:absolute;left:172px;top:217px;font-family:"Roboto",sans-serif;font-size:11px;color:var(--navy)}
.watermark{position:absolute;left:760px;top:70px;font-size:58px;font-weight:500;line-height:58px;color:#d7e6f0}

.field{position:absolute;left:499px}
.field svg{position:absolute;left:0;top:0}
.field label{position:absolute;left:14px;font-size:15px;color:#666}
.f-name{top:56px;width:280px;height:42px}
.f-name label{top:11px}
.f-mail{top:106px;width:269px;height:42px}
.f-mail label{top:11px}
.f-comments{top:156px;width:261px;height:94px}
.f-comments label{top:12px}
.field .ico{position:absolute}
.subscribe{position:absolute;left:766px;top:218px;width:142px;height:31px;background:var(--green-bright);color:var(--navy);font-size:19px;display:flex;align-items:center;justify-content:center}
</style>
</head>
<body>
<div class="top-bar"></div>

<section class="hero">
  <nav class="social" aria-label="Share">
    <span class="social-dot one" role="img" aria-label="Friendlink"></span>
    <span class="social-dot two" role="img" aria-label="Chirper"></span>
    <span class="social-dot three" aria-label="Email">
      <svg width="22" height="16" viewBox="0 0 22 16"><rect x="1" y="1" width="20" height="14" fill="none" stroke="#fff" stroke-width="1.6"/><path d="M1 1l10 8 10-8M1 15l7-6M21 15l-7-6" fill="none" stroke="#fff" stroke-width="1.4"/></svg>
    </span>
  </nav>

  <div class="brand">
    <span class="brand-dot"></span>
    <span class="brand-name">Solevia Labs</span>
  </div>

  <p class="welcome">Welcome to the new world of<br>3D Printing!</p>
  <h1 class="coming-soon">coming soon</h1>

  <div class="countdown">
    <div class="tick days"><span class="num">33</span><span class="unit">Days</span></div>
    <div class="tick lime"><span class="num">456</span><span class="unit">Hours</span></div>
    <div class="tick lime"><span class="num">59</span><span class="unit">Min</span></div>
    <div class="tick lime"><span class="num">30</span><span class="unit">Sec</span></div>
  </div>

  <div class="turing-btn">
    <svg width="30" height="36" viewBox="0 0 30 36"><rect x="3" y="4" width="22" height="29" rx="2" fill="none" stroke="#fff" stroke-width="2"/><rect x="9" y="1" width="10" height="6" rx="1" fill="#fff"/><path d="M7 13h14M7 18h14M7 23h10" stroke="#fff" stroke-width="1.6"/></svg>
    <span><span class="small">START A</span><span class="big">TURIN TEST</span></span>
  </div>
</section>

<section class="steps">
  <div class="step s1">
    <div class="step-photo photo-scan" role="img" aria-label="Tablet with a 3D scanner attached"></div>
    <div class="step-num">01</div>
    <div class="step-label">SCAN THE FOOT</div>
  </div>
  <div class="step s2">
    <div class="step-photo photo-design" role="img" aria-label="Orthotic design software showing a foot model"></div>
    <div class="step-num">02</div>
    <div class="step-label">DESIGN THE<br>ORTHOTIC</div>
  </div>
  <div class="step s3">
    <div class="step-photo photo-print" role="img" aria-label="Desktop 3D printer"></div>
    <div class="step-num">03</div>
    <div class="step-label">3D PRINT IT!</div>
  </div>
  <div class="step s4">
    <div class="step-photo photo-fit" role="img" aria-label="Hand placing an insole into a shoe"></div>
    <div class="step-num">04</div>
    <div class="step-label">FIT IT</div>
  </div>
</section>

<section class="notify">
  <h2 class="notify-title">GET NOTIFY WHEN WE LAUNCH</h2>
  <p class="pitch">Solevia Labs will shake up the Orthotics Industry. Foot Orthosis patient-ready in hours for a fraction of the price you are paying today.</p>
  <p class="copyright">Copyright 2014 © Solevia Labs All reserved</p>
  <div class="watermark" aria-hidden="true">Solevia<br>Labs</div>

  <form>
    <div class="field f-name">
      <svg width="280" height="42"><polygon points="0.5,0.5 279.5,0.5 272,41.5 0.5,41.5" fill="#fff" stroke="var(--field-line)"/></svg>
      <label>Name</label>
      <svg class="ico" style="left:246px;top:11px" width="18" height="20" viewBox="0 0 18 20"><circle cx="9" cy="6" r="5" fill="#ccc"/><path d="M0 20c0-6 4-8 9-8s9 2 9 8z" fill="#ccc"/></svg>
    </div>
    <div class="field f-mail">
      <svg width="269" height="42"><polygon points="0.5,0.5 268.5,0.5 261,41.5 0.5,41.5" fill="#fff" stroke="var(--field-line)"/></svg>
      <label>E-mail</label>
      <svg class="ico" style="left:232px;top:14px" width="22" height="15" viewBox="0 0 22 15"><rect x="1" y="1" width="20" height="13" fill="none" stroke="#ccc" stroke-width="1.4"/><path d="M1 1l10 7 10-7M1 14l7-6M21 14l-7-6" fill="none" stroke="#ccc" stroke-width="1.2"/></svg>
    </div>
    <div class="field f-comments">
      <svg width="261" height="94"><polygon points="0.5,0.5 260.5,0.5 244,93.5 0.5,93.5" fill="#fff" stroke="var(--field-line)"/></svg>
      <label>Comments</label>
    </div>
    <div class="subscribe">SUBSCRIBE</div>
  </form>
</section>

<div class="bottom-bar"></div>
</body>
</html>
```